MSA Plans

I would like to rebuild my brochure for the 3 business plans that I currently offer my clients. I would like to make it look much more modern & attractive to clients when choosing one of our service plans. If we can stick to a tech theme that would be great. Message me for anymore information.

```html
<!DOCTYPE html>
<html lang="en">
<head>
<meta charset="utf-8">
<title>MSA Plans – Managed Services Framework</title>
<link href="https://fonts.googleapis.com/css2?family=Cabin:wght@400;500;600&family=Nunito+Sans:wght@400;700;800&display=swap" rel="stylesheet">
<style>
  :root {
    --stage: #8e8f8e;
    --orange: #d9622b;
    --orange-bright: #e8622a;
    --ink: #231f20;
    --white: #ffffff;
    --peach: #fbdcc8;
    --rule: #b9b9b9;
    --tick: #2a9d3a;
    --cross: #e0201b;
  }
  * { margin: 0; padding: 0; box-sizing: border-box; }
  html, body { width: 1200px; height: 877px; overflow: hidden; }
  body {
    position: relative;
    background: var(--stage);
    font-family: "Cabin", sans-serif;
    color: var(--ink);
  }

  /* ---------- Cover page ---------- */
  .cover {
    position: absolute; left: 64px; top: 70px; width: 518px; height: 732px;
    overflow: hidden;
    background:
      radial-gradient(ellipse 85% 58% at 22% 14%, #ffffff 0%, rgba(255,255,255,.93) 38%, rgba(255,255,255,0) 100%),
      radial-gradient(ellipse 115% 70% at 0% 100%, var(--orange-bright) 0%, rgba(205,85,38,.85) 35%, rgba(120,45,20,0) 82%),
      linear-gradient(160deg, #d8d2ce 0%, #9a9290 26%, #3a2a26 56%, #0d0b0b 100%);
  }
  .cover-network {
    position: absolute; left: 0; right: 0; top: 380px; bottom: 0;
    background: radial-gradient(ellipse 60% 40% at 70% 50%, rgba(255,255,255,.05), rgba(255,255,255,0) 70%);
  }
  .brand {
    position: absolute; left: 66px; top: 78px;
    display: flex; align-items: center; gap: 9px;
  }
  .brand-dot { width: 26px; height: 26px; border-radius: 50%; background: var(--orange); }
  .brand-name {
    font-family: "Nunito Sans", sans-serif; font-weight: 800;
    font-size: 24px; letter-spacing: 1px; color: var(--orange); line-height: 1;
  }
  .brand-tagline {
    position: absolute; left: 101px; top: 103px;
    font-family: "Nunito Sans", sans-serif;
    font-size: 5.2px; font-weight: 700; letter-spacing: .8px; color: var(--ink);
  }
  .cover-title {
    position: absolute; left: 64px; top: 156px;
    font-family: "Cabin", sans-serif; font-weight: 500;
    font-size: 46px; line-height: 48px; color: var(--orange);
  }
  .cover-meta {
    position: absolute; left: 66px; top: 272px;
    font-family: "Cabin", sans-serif; font-size: 21px; line-height: 28px; color: var(--ink);
  }
  .cover-rule {
    position: absolute; left: 66px; top: 340px; width: 78px; height: 2px; background: var(--white);
  }
  .cover-tagline {
    position: absolute; left: 63px; top: 358px;
    font-family: "Nunito Sans", sans-serif; font-weight: 700;
    font-size: 19.5px; line-height: 25px; color: var(--white);
  }

  /* ---------- Plans page ---------- */
  .plans {
    position: absolute; left: 616px; top: 70px; width: 518px; height: 732px;
    overflow: hidden;
    background:
      radial-gradient(ellipse 55% 40% at 100% 90%, rgba(214,140,110,.9) 0%, rgba(160,80,140,.4) 45%, rgba(120,50,140,0) 80%),
      linear-gradient(165deg, #23a4d6 0%, #1b63ae 24%, #27307c 48%, #2b2266 68%, #5a2a8c 88%, #7a3a8f 100%);
  }
  .plans-network { position: absolute; inset: 0; }

  .plan-table {
    position: absolute; left: 31px; width: 454px;
    border-collapse: collapse; table-layout: fixed;
    font-family: "Cabin", sans-serif;
    font-size: 8.6px; line-height: 1.1;
  }
  .plan-table.msa { top: 32px; }
  .plan-table.cyber { top: 433px; }
  .plan-table tr { height: 13.4px; }
  .plan-table td, .plan-table th {
    padding: 0 3px; vertical-align: middle; white-space: nowrap; overflow: hidden;
  }
  .plan-table .head th {
    background: var(--ink); color: var(--white);
    font-family: "Nunito Sans", sans-serif;
    font-weight: 800; font-size: 8.6px; text-align: center;
  }
  .plan-table .head th:first-child { text-align: left; }
  .plan-table .section td {
    color: var(--white); font-family: "Nunito Sans", sans-serif; font-weight: 800; font-size: 8.6px;
    background: linear-gradient(90deg, #e0612a 0%, #b55a38 40%, #6c4a48 70%, #2a2224 100%);
  }
  .plan-table .item td {
    background: var(--white);
    border-bottom: 0.5px solid var(--rule);
    text-align: center;
  }
  .plan-table .item td + td { border-left: 0.5px solid var(--rule); }
  .plan-table .item td:first-child { text-align: left; }
  .plan-table .item.double { height: 26.8px; }
  .plan-table .item.double td:first-child { white-space: normal; line-height: 13.4px; }
  .plan-table .price td { background: var(--peach); text-align: center; }
  .plan-table .price td:first-child { text-align: left; }
  .plan-table.msa .price td { font-weight: 600; font-size: 8.8px; }

  .tick { color: var(--tick); font-weight: 600; }
  .cross { color: var(--cross); font-weight: 700; }

  .plans-footer {
    position: absolute; left: 0; right: 0; top: 686px;
    text-align: center; color: var(--white);
    font-family: "Cabin", sans-serif;
    font-size: 7.3px; line-height: 10px;
  }
</style>
</head>
<body>

<section class="cover">
  <div class="cover-network" role="img" aria-label="Glowing network of connected nodes and lines across the lower page"></div>
  <div class="brand">
    <span class="brand-dot"></span>
    <span class="brand-name">NORTHWIRE</span>
  </div>
  <div class="brand-tagline">MANAGED I.T SUPPORT FOR GROWING TEAMS</div>
  <h1 class="cover-title">Managed Services<br>Framework</h1>
  <p class="cover-meta">Version 1.0<br>Updated: April 2024</p>
  <div class="cover-rule"></div>
  <p class="cover-tagline">Defining our services and how<br>we deliver these consistently to you.</p>
</section>

<section class="plans">
  <div class="plans-network" role="img" aria-label="Blue and purple technology network of nodes and connecting lines"></div>

  <table class="plan-table msa">
    <colgroup><col style="width:219px"><col><col><col></colgroup>
    <tr class="head"><th>Managed Services Agreement</th><th>Essential</th><th>Business</th><th>Professional</th></tr>
    <tr class="section"><td colspan="4">Support</td></tr>
    <tr class="item"><td>Unlimited Remote Support 7am to 6pm</td><td class="tick">✓</td><td class="tick">✓</td><td class="tick">✓</td></tr>
    <tr class="item"><td>3rd Party Vendor Support</td><td class="tick">✓</td><td class="tick">✓</td><td class="tick">✓</td></tr>
    <tr class="item"><td>Reactive Onsite Support 8am to 5pm</td><td>VIP Rates</td><td class="tick">✓</td><td class="tick">✓</td></tr>
    <tr class="item"><td>After-Hours Support</td><td>VIP Rates</td><td>VIP Rates</td><td class="tick">✓</td></tr>
    <tr class="section"><td colspan="4">Service</td></tr>
    <tr class="item"><td>Guaranteed SLA Response Times</td><td class="tick">✓</td><td class="tick">✓</td><td class="tick">✓</td></tr>
    <tr class="item"><td>24x7 Website &amp; Infrastructure Monitoring</td><td class="tick">✓</td><td class="tick">✓</td><td class="tick">✓</td></tr>
    <tr class="item"><td>SecureWeb Content Filtering</td><td></td><td class="tick">✓</td><td class="tick">✓</td></tr>
    <tr class="item"><td>Backup Monitoring</td><td class="tick">✓</td><td class="tick">✓</td><td class="tick">✓</td></tr>
    <tr class="item"><td>Desktop OS Patching &amp; Updating</td><td class="tick">✓</td><td class="tick">✓</td><td class="tick">✓</td></tr>
    <tr class="item"><td>CEO / MD Home Tech Support</td><td class="tick">✓</td><td class="tick">✓</td><td class="tick">✓</td></tr>
    <tr class="item"><td>Monthly Tech Site Visit</td><td class="cross">✘</td><td>Quarterly</td><td>Monthly</td></tr>
    <tr class="item"><td>Short Term Loan Equipment</td><td class="cross">✘</td><td>1 Month</td><td>3 Months</td></tr>
    <tr class="item"><td>Adds / Moves / Changes (Staff)</td><td class="tick">✓</td><td class="tick">✓</td><td class="tick">✓</td></tr>
    <tr class="item"><td>Adds / Moves / Changes (Workstations)</td><td>VIP Rates</td><td>VIP Rates</td><td class="tick">✓</td></tr>
    <tr class="section"><td colspan="4">Management</td></tr>
    <tr class="item"><td>Asset and Warranty Tracking &amp; Reporting</td><td class="tick">✓</td><td class="tick">✓</td><td class="tick">✓</td></tr>
    <tr class="item"><td>Comprehensive IT Documentation</td><td class="tick">✓</td><td class="tick">✓</td><td class="tick">✓</td></tr>
    <tr class="item"><td>Technology Strategy Meeting</td><td>Annual</td><td>Quarterly</td><td>Monthly</td></tr>
    <tr class="item"><td>Technology Business Review Meeting</td><td>Annual</td><td>Bi Annual</td><td>Quarterly</td></tr>
    <tr class="item"><td>IT Policy Templates</td><td class="cross">✘</td><td class="tick">✓</td><td class="tick">✓</td></tr>
    <tr class="section"><td colspan="4">Training</td></tr>
    <tr class="item"><td>End User Training Materials</td><td class="cross">✘</td><td class="cross">✘</td><td class="tick">✓</td></tr>
    <tr class="item"><td>Security Awareness Training</td><td class="tick">✓</td><td class="tick">✓</td><td class="tick">✓</td></tr>
    <tr class="price"><td>RRP / User</td><td>$110</td><td>$130</td><td>$165</td></tr>
    <tr class="price"><td>Minimum User Count</td><td>5</td><td>5</td><td>5</td></tr>
    <tr class="price"><td>Minimum Monthly Commit</td><td>$550</td><td>$650</td><td>$825</td></tr>
  </table>

  <table class="plan-table cyber">
    <colgroup><col style="width:298px"><col><col></colgroup>
    <tr class="head"><th>Cybersecurity Packages</th><th>Business</th><th>Professional</th></tr>
    <tr class="item"><td>Compliance with Core Cyber Baseline Maturity</td><td>Level 0</td><td>Level 1</td></tr>
    <tr class="item"><td>Security Standard - Alignment to Northwire Cloud Security Policy &amp; Reporting</td><td class="tick">✓</td><td class="tick">✓</td></tr>
    <tr class="item"><td>24x7 Security Operations Centre (SOC) - Monitoring Cloud Mail &amp; Files</td><td class="tick">✓</td><td class="tick">✓</td></tr>
    <tr class="item"><td>DarkWeb Scanning</td><td class="tick">✓</td><td class="tick">✓</td></tr>
    <tr class="item"><td>Cloud Email Filtering</td><td class="tick">✓</td><td class="tick">✓</td></tr>
    <tr class="item"><td>Cloud Workspace Backup</td><td class="tick">✓</td><td class="tick">✓</td></tr>
    <tr class="item"><td>Automated Email Signatures</td><td class="tick">✓</td><td class="tick">✓</td></tr>
    <tr class="item"><td>Endpoint Protection with EDR - Workstations &amp; Servers</td><td class="tick">✓</td><td class="tick">✓</td></tr>
    <tr class="item"><td>3rd Party Applications Updating</td><td class="cross">✘</td><td class="tick">✓</td></tr>
    <tr class="item"><td>24x7 Security Operations Centre (SOC) - Monitoring Endpoints and Servers</td><td class="cross">✘</td><td class="tick">✓</td></tr>
    <tr class="item"><td>Privileged Access Management &amp; Application Whitelisting</td><td class="cross">✘</td><td class="tick">✓</td></tr>
    <tr class="item"><td>Internal Vulnerability Scanning</td><td class="cross">✘</td><td class="tick">✓</td></tr>
    <tr class="item double"><td>Backup &amp; Disaster Recovery to comply with Core Cyber Baseline Level 1<br>Assessment</td><td class="cross">✘</td><td>Pending</td></tr>
    <tr class="price"><td>RRP / User</td><td>$35</td><td>$60</td></tr>
    <tr class="price"><td>Minimum User Count</td><td>5</td><td>5</td></tr>
    <tr class="price"><td>Minimum Monthly Commit</td><td>$175</td><td>$300</td></tr>
  </table>

  <footer class="plans-footer">
    NORTHWIRE TECHNOLOGY PTY LTD | ABN: 12 345 678 901<br>
    northwiretech.example | service@northwiretech.example | 4/18 Example St, Sampleton, VIC, 3000 | 1300 000 111
  </footer>
</section>

</body>
</html>
```